One pager digital ad-Corporate travel Manager

I need a design that is smooth, and business like. I don’t like basic generic designs that I can make my self. I’m looking for a sharp clean ad that clearly was made by a great designer. I need some bullet points in and the add to be clean. Here is a list of some content from our content writers. You can arrange and play with the words a bit.

*Budget*- having a travel management service will ensure that your company sticks to a budget which will help PROTECT your bottom line. Travel expenses often CAN BE COSTLY and having a SAVVY corporate travel manager handle YOUR TRAVEL ARRANGEMENTS will make sure that the travel expenses are kept under control.
*Efficiency- time *is money. Have your staff focus on their core business and have the corporate travel manager handle all the logistics for their travel including airfare, hotel cars and events TO MAXIMIZE EFFICIENCY AND KEEP YOUR STAFF FOCUSED ON YOUR CORE BUSINESS

*unforeseen circumstances* – the corporate travel manager handleS any cancellations, missed flights, canceled flights. Quick rebooking, and repositioning, and dealing with getting credits and reimbursement is extremely difficult and time-consuming. The corporate travel manager handles all of that SO YOU CAN CONTINUE ON SCHEDULE WITHOUT SPENDING HOURS REBOOKING AND GETTING CREDIT

Efficient and organized business travel management-help reduce travel expenses, streamline expense reports, optimize booking processes, and make managing the corporate travel experience way easier for all stakeholders involved.

Travel Support

Report on travel spend: In order to optimize their budgets, businesses need to know which departments are spending what on travel. Agencies can report on spend for all stakeholders by team, department, or project, and help you accurately track all your travel expenses.

Maintain compliance: Every company has some sort of rules that make up their travel policy. An agency can enforce these guidelines when booking.

Velmora Journeys is a global leader in business travel management services. We drive savings, efficiency and safety to businesses and their travelers all around the world.

If you are looking for a tailored travel management solution, delivering customer service excellence, and a demonstrable return on investment, then you’ve come to the right place

Corporate travel policy compliance
Travel management reports
Meetings and event management
Travel program management
Dedicated travel counselor teams

By listening to your needs and focusing on your goals we can help your company design a global corporate travel service program that controls costs, improves traveler satisfaction and fits your corporate culture.

Our qualified business travel agents and cutting-edge technology deliver solutions that provide the best travel arrangements and travel policy adherence in the business. From CEO to support staff, our services can help make corporate travel a more efficient and enjoyable experience for everyone involved.

With so much involved in travel – from booking and expenses to meetings and strategy – you need the backing of a proven leader…
Velmora Journeys, We’re your corporate travel partner to help you manage it all.

```html
<!DOCTYPE html>
<html lang="en">
<head>
<meta charset="utf-8">
<title>Velmora Journeys – Corporate Travel Flyer</title>
<link href="https://fonts.googleapis.com/css2?family=Montserrat:wght@500;600;700;800&family=Poppins:wght@400;500;600&display=swap" rel="stylesheet">
<style>
  :root{
    --navy-deep:#0a2150;
    --navy:#0e2a5e;
    --blue:#153f80;
    --cyan:#1fc7e6;
    --cyan-soft:#c2f1f8;
    --ink:#23314a;
    --muted-blue:#3a5d94;
    --page:#ffffff;
    --backdrop:#eef1f4;
  }
  *{box-sizing:border-box;margin:0;padding:0}
  html,body{width:1200px;height:2400px;overflow:hidden;background:var(--backdrop)}
  body{position:relative;font-family:"Poppins",sans-serif;color:var(--ink)}

  .flyer{position:absolute;left:50px;top:488px;width:933px;height:1208px;
    transform:scale(1.179);transform-origin:0 0;background:var(--page);overflow:hidden;
    box-shadow:0 6px 24px rgba(10,33,80,.18)}

  .hero{position:absolute;left:0;top:0;width:933px;height:344px;
    background:linear-gradient(120deg,#0b2352 0%,#123a70 45%,#0d2b5c 100%)}
  .hero-band{position:absolute;left:0;top:344px;width:933px;height:119px;background:var(--cyan)}
  .hero-photo{position:absolute;left:580px;top:0;width:353px;height:418px;
    background:linear-gradient(160deg,#2b3a4a 0%,#56606a 40%,#c8432e 70%,#3a4350 100%);
    clip-path:polygon(8% 0,100% 0,100% 100%,0 100%,0 30%)}

  .brand{position:absolute;left:40px;top:124px;width:200px;display:flex;align-items:center;justify-content:center;gap:8px;
    font-family:"Montserrat",sans-serif;font-weight:500;font-size:13px;letter-spacing:2px;color:#ffffff;white-space:nowrap}
  .brand-dot{width:9px;height:9px;border-radius:50%;background:#ffffff;flex:none}

  .headline{position:absolute;left:37px;top:176px;font-family:"Montserrat",sans-serif;font-weight:800;line-height:.9;white-space:nowrap}
  .headline .line-1{display:block;font-size:76px;color:#fff}
  .headline .line-2{display:block;font-size:66px;color:var(--cyan);margin-top:4px}

  .intro{position:absolute;left:40px;top:362px;width:540px}
  .intro-title{font-family:"Montserrat",sans-serif;font-weight:700;font-size:19px;line-height:1.2;color:#fff}
  .intro-text{font-size:13px;line-height:15px;margin-top:6px;color:var(--navy-deep)}

  .benefit-label{position:absolute;left:40px;height:28px;width:207px;background:var(--cyan-soft);color:var(--blue);
    font-family:"Montserrat",sans-serif;font-weight:700;font-size:16px;line-height:28px;padding-left:10px}
  .benefit-label.wide{width:370px}
  .benefit-text{position:absolute;left:44px;width:362px;font-size:11.6px;line-height:14.7px;letter-spacing:-.1px;color:var(--ink)}
  .benefit-text strong{font-weight:600}
  .label-budget{top:481px}
  .text-budget{top:515px}
  .label-efficiency{top:615px}
  .text-efficiency{top:649px}
  .label-unforeseen{top:736px}
  .text-unforeseen{top:772px}
  .text-closing{top:889px}

  .support{position:absolute;left:448px;top:436px;width:442px;height:522px;border-radius:16px;overflow:hidden;background:var(--cyan-soft)}
  .support-title{background:var(--navy-deep);height:75px;color:var(--cyan);
    font-family:"Montserrat",sans-serif;font-weight:800;font-size:36px;padding:12px 0 0 32px}
  .support-item{height:117px;padding:15px 67px 0 30px;color:#fff}
  .support-item:nth-of-type(odd){background:var(--blue)}
  .support-item:nth-of-type(even){background:var(--navy-deep)}
  .support-item h3{font-family:"Montserrat",sans-serif;font-weight:700;font-size:11px;margin-bottom:5px}
  .support-item p{font-size:12px;line-height:14.7px;letter-spacing:-.1px}
  .support-item-last{height:126px;border-radius:0 0 16px 16px}
  .support-note{padding:12px 28px 0 31px;font-family:"Montserrat",sans-serif;font-weight:700;font-size:13.4px;line-height:16.5px;color:var(--navy)}

  .services{position:absolute;left:50px;top:976px;width:835px;height:90px;background:var(--blue);border-radius:10px;display:flex}
  .service{flex:1;padding:12px 0 0 22px;color:#fff;border-right:1px solid rgba(255,255,255,.12);
    font-family:"Montserrat",sans-serif;font-size:13.4px;line-height:16.5px;font-weight:600}
  .service:last-child{border-right:none}
  .service svg{display:block;margin-bottom:4px}

  .cta{position:absolute;left:70px;top:1082px;font-family:"Montserrat",sans-serif;font-weight:800;color:var(--blue);line-height:1;white-space:nowrap}
  .cta .cta-big{font-size:23px;display:block}
  .cta .cta-small{font-size:15px;line-height:16px;display:block;color:var(--muted-blue);margin-top:2px}
  .cta-box{position:absolute;left:215px;top:1082px;width:634px;height:56px;border:1.5px dashed var(--blue);border-radius:6px;display:flex;align-items:center;justify-content:space-around}
  .cta-item{display:flex;align-items:center;gap:10px;font-family:"Montserrat",sans-serif;font-size:13.4px;line-height:16px;color:var(--navy-deep);font-weight:500;white-space:nowrap}

  .website{position:absolute;left:0;top:1156px;width:933px;text-align:center;font-family:"Montserrat",sans-serif;font-weight:700;font-size:23px;letter-spacing:5px;color:var(--navy)}
</style>
</head>
<body>
<div class="flyer">
  <div class="hero"></div>
  <div class="hero-band"></div>
  <div class="hero-photo" role="img" aria-label="Photo of two business travellers with a suitcase resting at the open tailgate of a car"></div>

  <div class="brand"><span class="brand-dot"></span>VELMORA JOURNEYS</div>

  <h1 class="headline"><span class="line-1">VELMORA</span><span class="line-2">JOURNEYS</span></h1>

  <div class="intro">
    <div class="intro-title">We’re your corporate travel partner<br>to help you manage it all.</div>
    <div class="intro-text">With so much involved in travel – from booking and expenses to meetings<br>and strategy – you need the backing of a proven leader</div>
  </div>

  <div class="benefit-label label-budget">BUDGET</div>
  <p class="benefit-text text-budget">having a travel management service will ensure that your company sticks to a budget which will help PROTECT your bottom line. Travel expenses often CAN BE COSTLY and having a SAVVY corporate travel manager handle YOUR TRAVEL ARRANGEMENTS will make sure that the travel expenses are kept under control.</p>

  <div class="benefit-label label-efficiency">EFFICIENCY</div>
  <p class="benefit-text text-efficiency">time is money. Have your staff focus on their core business and have the corporate travel manager handle all the logistics for their travel including airfare, hotel cars and events TO MAXIMIZE EFFICIENCY AND KEEP YOUR STAFF FOCUSED ON YOUR CORE BUSINESS</p>

  <div class="benefit-label wide label-unforeseen">UNFORESEEN CIRCUMSTANCES</div>
  <p class="benefit-text text-unforeseen">the corporate travel manager handleS any cancellations, missed flights, canceled flights. Quick rebooking, and repositioning, and dealing with getting credits and reimbursement is extremely difficult and time-consuming. The corporate travel manager handles all of that SO YOU CAN CONTINUE ON SCHEDULE WITHOUT SPENDING HOURS <strong>REBOOKING AND GETTING CREDIT</strong></p>

  <p class="benefit-text text-closing">Efficient and organized business travel management-help reduce travel expenses, streamline expense reports, optimize booking processes, and make managing the corporate travel experience way easier for all stakeholders involved.</p>

  <section class="support">
    <h2 class="support-title">TRAVEL SUPPORT</h2>
    <div class="support-item">
      <h3>REPORT ON TRAVEL SPEND</h3>
      <p>In order to optimize their budgets, businesses need to know which departments are spending what on travel. Agencies can report on spend for all stakeholders by team, department, or project, and help you accurately track all your travel expenses.</p>
    </div>
    <div class="support-item">
      <h3>REPORT ON TRAVEL SPEND</h3>
      <p>In order to optimize their budgets, businesses need to know which departments are spending what on travel. Agencies can report on spend for all stakeholders by team, department, or project, and help you accurately track all your travel expenses.</p>
    </div>
    <div class="support-item support-item-last">
      <h3>REPORT ON TRAVEL SPEND</h3>
      <p>In order to optimize their budgets, businesses need to know which departments are spending what on travel. Agencies can report on spend for all stakeholders by team, department, or project, and help you accurately track all your travel expenses.</p>
    </div>
    <p class="support-note">Velmora Journeys is a global leader in business travel management services. We drive savings, efficiency and safety to businesses and their travelers all around the world.</p>
  </section>

  <div class="services">
    <div class="service"><svg width="11" height="11" viewBox="0 0 11 11"><rect x=".7" y=".7" width="9.6" height="9.6" fill="none" stroke="#1fc7e6" stroke-width="1.2"/><path d="M2.5 5.5l2 2 4-5" fill="none" stroke="#1fc7e6" stroke-width="1.4"/></svg>Corporate<br>travel policy<br>compliance</div>
    <div class="service"><svg width="11" height="11" viewBox="0 0 11 11"><rect x=".7" y=".7" width="9.6" height="9.6" fill="none" stroke="#1fc7e6" stroke-width="1.2"/><path d="M2.5 5.5l2 2 4-5" fill="none" stroke="#1fc7e6" stroke-width="1.4"/></svg>Travel<br>management<br>reports</div>
    <div class="service"><svg width="11" height="11" viewBox="0 0 11 11"><rect x=".7" y=".7" width="9.6" height="9.6" fill="none" stroke="#1fc7e6" stroke-width="1.2"/><path d="M2.5 5.5l2 2 4-5" fill="none" stroke="#1fc7e6" stroke-width="1.4"/></svg>Meetings<br>and event<br>management</div>
    <div class="service"><svg width="11" height="11" viewBox="0 0 11 11"><rect x=".7" y=".7" width="9.6" height="9.6" fill="none" stroke="#1fc7e6" stroke-width="1.2"/><path d="M2.5 5.5l2 2 4-5" fill="none" stroke="#1fc7e6" stroke-width="1.4"/></svg>Travel<br>program<br>management</div>
    <div class="service"><svg width="11" height="11" viewBox="0 0 11 11"><rect x=".7" y=".7" width="9.6" height="9.6" fill="none" stroke="#1fc7e6" stroke-width="1.2"/><path d="M2.5 5.5l2 2 4-5" fill="none" stroke="#1fc7e6" stroke-width="1.4"/></svg>Dedicated<br>travel counselor<br>teams</div>
  </div>

  <div class="cta"><span class="cta-big">IF YOU ARE</span><span class="cta-small">LOOKING FOR A<br>TAILORED TRAVEL</span></div>
  <div class="cta-box">
    <div class="cta-item">
      <svg width="30" height="28" viewBox="0 0 30 28"><circle cx="11" cy="7" r="6" fill="#0e2a5e"/><path d="M0 28c0-8 5-12 11-12s8 2 9 4v8z" fill="#0e2a5e"/><circle cx="23" cy="22" r="5" fill="none" stroke="#0e2a5e" stroke-width="3" stroke-dasharray="2.5 1.4"/></svg>
      <span>Managment<br>solution</span>
    </div>
    <div class="cta-item">
      <svg width="30" height="28" viewBox="0 0 30 28"><circle cx="15" cy="6" r="5" fill="#0e2a5e"/><path d="M8 20c0-5 3-8 7-8s7 3 7 8z" fill="#0e2a5e"/><path d="M2 18l8 6h16l2-4" fill="none" stroke="#0e2a5e" stroke-width="3"/></svg>
      <span>Delivering customer<br>service excellence</span>
    </div>
    <div class="cta-item">
      <svg width="30" height="30" viewBox="0 0 30 30"><circle cx="17" cy="8" r="7" fill="#0e2a5e"/><text x="17" y="12" text-anchor="middle" font-size="10" font-family="Montserrat,sans-serif" font-weight="800" fill="#fff">$</text><path d="M2 20h8l6 3h10v3H14l-6-2H2z" fill="#0e2a5e"/></svg>
      <span>Demonstrable return<br>on investment</span>
    </div>
  </div>

  <div class="website">www.velmorajourneys.com</div>
</div>
</body>
</html>
```